Hollowmere Dental Center Specials/Offers

Take the advertisement pic (LABELED ADVERTISEMENT) and make it look "professional in appearance" using the logo and color scheme of Hollowmere Dental Center. The Phone number should be 719-555-0186. I want the same content, different background, professional looking document. I want it to be a 12"x12" document. High resolution files should include .PDF, .JPG and .AI. Any or all documents can be used for colors and overall scheme. I would like to have the overall colors include the main blue color from the file 4db749b4ef4c5e0717512bf7eb26bf54 and include the brown "swoosh" somewhere through/on the final document. Stock files of smiling young families can be used but not required. I am on a tight time-line and have placed 5 days as the deadline, but I will pick my favorite in as little as 2-3 days if I can get a good product. Again ALL the info from the Advertisement document should be included on the final product. Use any or all of the uploaded files for assistance. You can also visit our website for more info: www.hollowmeredentalcenter.example Thanks

```html
<!DOCTYPE html>
<html lang="en">
<head>
<meta charset="utf-8">
<title>Hollowmere Dental Center – Family Advertisement</title>
<link href="https://fonts.googleapis.com/css2?family=Alegreya:ital@1&family=Didact+Gothic&family=PT+Sans:wght@400;700&display=swap" rel="stylesheet">
<style>
  :root {
    --page-bg: #e9ecee;
    --sky-top: #ffffff;
    --sky-mid: #d9eef2;
    --sky-low: #9fd0da;
    --teal: #4a9aab;
    --brand-ink: #4a4340;
    --brand-teal: #4d8796;
    --headline-brown: #5b4a43;
    --white: #ffffff;
  }
  * { margin: 0; padding: 0; box-sizing: border-box; }
  html, body { width: 1019px; height: 1200px; overflow: hidden; }
  body { background: var(--page-bg); position: relative; }

  .ad {
    position: absolute; left: 0; top: 90px;
    width: 1019px; height: 1019px; overflow: hidden;
    background: linear-gradient(180deg, var(--sky-top) 0%, var(--sky-mid) 28%, var(--sky-low) 48%, var(--teal) 66%);
  }

  .family-photo {
    position: absolute; left: 400px; top: 140px;
    width: 600px; height: 520px;
    background: radial-gradient(ellipse 50% 50% at 55% 50%, rgba(233,214,200,0.95) 0%, rgba(207,180,162,0.85) 40%, rgba(169,195,204,0.5) 70%, rgba(169,195,204,0) 100%);
  }

  .wave { position: absolute; left: 0; top: 0; width: 1019px; height: 1019px; }

  .brand {
    position: absolute; left: 100px; top: 160px;
    font-family: "Didact Gothic", sans-serif; color: var(--brand-ink);
  }
  .brand-name {
    display: flex; align-items: center; gap: 14px;
    font-size: 38px; line-height: 1.1;
  }
  .brand-dot { width: 22px; height: 22px; border-radius: 50%; background: var(--brand-teal); flex: none; }
  .brand-tagline {
    margin-top: 10px; margin-left: 2px;
    font-size: 18px; letter-spacing: 1.5px; white-space: nowrap;
  }

  .headline {
    position: absolute; left: 49px; top: 728px;
    font-family: "Alegreya", serif; font-style: italic; font-weight: 400;
    font-size: 56px; color: var(--headline-brown); white-space: nowrap;
  }

  .practice {
    position: absolute; left: 49px; top: 872px;
    font-family: "PT Sans", sans-serif; color: var(--white);
  }
  .doctor { font-weight: 700; font-size: 26px; margin-bottom: 12px; }
  .doctor small { font-size: 21px; }
  .address { font-size: 22px; line-height: 31px; }

  .contacts {
    position: absolute; left: 559px; top: 852px;
    list-style: none;
    font-family: "PT Sans", sans-serif; font-size: 22px; line-height: 31px; color: var(--white);
  }
  .contacts li { display: flex; align-items: center; gap: 8px; white-space: nowrap; }
  .contacts svg { width: 20px; height: 20px; fill: var(--white); flex: none; }
</style>
</head>
<body>
  <main class="ad">
    <div class="family-photo" role="img" aria-label="Photo of a smiling couple embracing, cheek to cheek"></div>

    <svg class="wave" viewBox="0 0 1019 1019" aria-hidden="true">
      <defs>
        <linearGradient id="band" x1="0" y1="0" x2="0" y2="1">
          <stop offset="0" stop-color="#5aa8b8"/>
          <stop offset="0.3" stop-color="#4a9aab"/>
          <stop offset="1" stop-color="#4697a8"/>
        </linearGradient>
      </defs>
      <path d="M0,345 C260,450 520,640 1019,630 L1019,1019 L0,1019 Z" fill="#8fc7d3" opacity="0.45"/>
      <path d="M0,400 C300,520 560,690 1019,660 L1019,1019 L0,1019 Z" fill="url(#band)"/>
      <path d="M0,318 C260,430 520,630 1019,638" fill="none" stroke="#ffffff" stroke-width="3" opacity="0.9"/>
      <path d="M0,334 C280,450 540,650 1019,648" fill="none" stroke="#ffffff" stroke-width="1.5" opacity="0.6"/>
      <path d="M0,420 C320,560 600,720 1019,672" fill="none" stroke="#ffffff" stroke-width="2" opacity="0.35"/>
    </svg>

    <div class="brand">
      <div class="brand-name"><span class="brand-dot"></span><span>Hollowmere<br>Dental Center</span></div>
      <p class="brand-tagline">FAMILY • COSMETIC • IMPLANTS</p>
    </div>

    <h1 class="headline">Where the Whole Family can be Seen!</h1>

    <section class="practice">
      <p class="doctor">MARTIN L. HOLLOWMERE | <small>D.D.S.</small></p>
      <p class="address">4820 Aspen Ridge Dr. Suite B<br>Colorado Springs, CO 80999</p>
    </section>

    <ul class="contacts">
      <li><svg viewBox="0 0 24 24"><path d="M6.6 2.5l3 .4 1.2 4.8-2.2 1.6c1 2.4 2.7 4.3 5 5.6l1.8-2.1 4.7 1.4.3 3.1c-.1 1.5-1.5 2.7-3 2.6C9.6 19.3 4.5 14 4 6.2c-.1-1.9 1-3.5 2.6-3.7z"/></svg>(719) 555-0186</li>
      <li><svg viewBox="0 0 24 24"><path d="M6 3h12v5H6zM3 9h18v8h-3v4H6v-4H3zm5 6v4h8v-4z"/></svg>(719) 555-0142</li>
      <li><svg viewBox="0 0 24 24"><path d="M2 5h20v14H2zm2 2v.4l8 5.3 8-5.3V7zm0 2.8V17h16V9.8l-8 5.3z"/></svg>hollowmeredentalcenter@example.com</li>
      <li><svg viewBox="0 0 24 24"><path d="M12 2a10 10 0 100 20 10 10 0 000-20zm0 2c.9 0 2.2 1.6 2.8 5H9.2C9.8 5.6 11.1 4 12 4zM4.3 10h3.5a17 17 0 000 4H4.3a8 8 0 010-4zm5 0h5.4a15 15 0 010 4H9.3a15 15 0 010-4zm6.9 0h3.5a8 8 0 010 4h-3.5a17 17 0 000-4zM12 20c-.9 0-2.2-1.6-2.8-5h5.6c-.6 3.4-1.9 5-2.8 5z"/></svg>www.hollowmeredentalcenter.example</li>
    </ul>
  </main>
</body>
</html>
```